WWW.VELTRONA.IT BUSINNES CARD

WE NEED A BUSINESS CARD . I HAVE A COMPANY IN ITALY NR 1 IN HAIR MEDICAL CARE AN HAIR REPLECEMENT . IN CARD I NEED WRITE WEB ADDRESS, MAIL , ADDRESS, TELEPHONE NUMBER , AND NAME
IN THE BACK SIDE I NEED MY DOCTOR LOGO .
MY WEB SITE IS WWW.VELTRONA.IT
Updates

Target Market(s)

CONSUMER B2C

Industry/Entity Type

Hair And Beauty

Contact Information for Business Card

I WANT A MEDICAL BUSINESS CARD.

Font styles to use
Other font styles liked:
• VERDANA

Colors
33a6d7
3176b5
85abd2
aedbee
eaf1f7
ffffff

Requirements
Must have
• I NEED MY LOGO AND LOGO OF DR VELTRONA

```html
<!DOCTYPE html>
<html lang="it">
<head>
<meta charset="utf-8">
<title>Veltrona – Business Card</title>
<link rel="stylesheet" href="https://fonts.googleapis.com/css2?family=Montserrat:wght@300;400;800&family=Open+Sans:wght@400;600;700&display=swap">
<style>
  :root{
    --blue-main:#33a6d7;
    --blue-bright:#12b3e8;
    --blue-deep:#3176b5;
    --blue-soft:#85abd2;
    --blue-pale:#aedbee;
    --blue-mist:#eaf1f7;
    --white:#ffffff;
    --stage:#e9edf1;
  }
  *{box-sizing:border-box;margin:0;padding:0}
  html,body{width:1200px;height:900px;overflow:hidden;background:var(--stage)}
  .stage{width:1200px;height:900px;display:flex;align-items:center;justify-content:center;gap:40px}
  .card{width:540px;height:310px;border-radius:26px;position:relative;overflow:hidden;box-shadow:0 10px 30px rgba(30,60,90,.18)}

  /* front */
  .card--front{background:linear-gradient(160deg,var(--blue-main) 0%,var(--blue-bright) 100%);color:var(--white);font-family:"Open Sans",Verdana,sans-serif}
  .card--front .edge-band{position:absolute;left:0;right:0;bottom:0;height:16px;background:var(--white)}
  .person{position:absolute;left:36px;top:52px}
  .person__first{font-family:"Montserrat",sans-serif;font-weight:800;font-size:32px;letter-spacing:2px;line-height:1}
  .person__last{font-family:"Montserrat",sans-serif;font-weight:300;font-size:32px;letter-spacing:3px;line-height:1.2}
  .person__role{display:inline-block;margin-top:12px;background:var(--white);color:var(--blue-main);font-family:"Montserrat",sans-serif;font-weight:400;font-size:11px;letter-spacing:2.5px;padding:6px 14px;border-radius:14px}
  .brand{position:absolute;right:40px;top:48px}
  .brand__row{display:flex;align-items:center;gap:8px}
  .brand__dot{width:16px;height:16px;border-radius:50%;background:var(--white)}
  .brand__name{font-weight:700;font-size:24px;letter-spacing:.5px}
  .contacts{position:absolute;left:292px;top:128px;list-style:none;width:218px}
  .contacts li{display:flex;align-items:center;gap:10px;font-size:15px;padding:6px 0;border-bottom:1px solid rgba(255,255,255,.75);white-space:nowrap}
  .contacts li:last-child{border-bottom:none}
  .contacts svg{width:14px;height:14px;flex:none}

  /* back */
  .card--back{background:var(--white);display:flex;align-items:center;justify-content:center;font-family:"Open Sans",Verdana,sans-serif}
  .brand-large .brand__row{gap:12px}
  .brand-large .brand__dot{width:30px;height:30px;background:var(--blue-main)}
  .brand-large .brand__name{font-size:50px;color:var(--blue-deep)}
</style>
</head>
<body>
<main class="stage">

  <section class="card card--front" aria-label="Fronte del biglietto">
    <div class="person">
      <div class="person__first">DAVIDE</div>
      <div class="person__last">FERRANTE</div>
      <div class="person__role">HAIR SPECIALIST</div>
    </div>

    <div class="brand">
      <div class="brand__row"><span class="brand__dot"></span><span class="brand__name">VELTRONA</span></div>
    </div>

    <ul class="contacts">
      <li>
        <svg viewBox="0 0 24 24" fill="none" stroke="#fff" stroke-width="2"><path d="M5 3h4l2 5-3 2a12 12 0 0 0 6 6l2-3 5 2v4a2 2 0 0 1-2 2A18 18 0 0 1 3 5a2 2 0 0 1 2-2z"/></svg>
        045 00 12 34
      </li>
      <li>
        <svg viewBox="0 0 24 24" fill="none" stroke="#fff" stroke-width="2"><rect x="3" y="5" width="18" height="14"/><path d="M3 5l9 8 9-8"/></svg>
        info@veltrona.it
      </li>
      <li>
        <svg viewBox="0 0 24 24" fill="none" stroke="#fff" stroke-width="2"><circle cx="12" cy="12" r="9"/><path d="M3 12h18M12 3c3 3 3 15 0 18M12 3c-3 3-3 15 0 18"/></svg>
        www.veltrona.it
      </li>
      <li>
        <svg viewBox="0 0 24 24" fill="none" stroke="#fff" stroke-width="2"><path d="M12 22s7-7 7-12a7 7 0 0 0-14 0c0 5 7 12 7 12z"/><circle cx="12" cy="10" r="2.5"/></svg>
        via Castelmare 8 Verona
      </li>
    </ul>

    <div class="edge-band"></div>
  </section>

  <section class="card card--back" aria-label="Retro del biglietto">
    <div class="brand-large">
      <div class="brand__row"><span class="brand__dot"></span><span class="brand__name">VELTRONA</span></div>
    </div>
  </section>

</main>
</body>
</html>
```